A Recruitment Company Needs a Web Design that Expresses High Energy and Results

Our company, BrightLane Consultants, needs a web design for our recruiting business based in Asia (Taiwan). We provide recruitment services to many international companies. Our client base is as follows:
Hi-Tech - 60%
Healthcare and Consumer/FMCG - 15%
Industrial and Engineering - 15%
Banking and Finance - 10%

The website will be accessed by both clients and job seekers. As such, it should look professional, user-friendly and is interactive.

Industry/Entity Type

Business

Coding

Coded - Design and coding required

Number of Pages Required

5+ page

Font styles to use
Sans Serif

Colors
add136
ffffff
000000

Requirements
Must have
• Attached is the company's logo. the design mus be in line with it.

```html
<!DOCTYPE html>
<html lang="en">
<head>
<meta charset="utf-8">
<title>BrightLane Consultants</title>
<link href="https://fonts.googleapis.com/css2?family=Roboto:wght@300;400;500;700&display=swap" rel="stylesheet">
<style>
:root{
  --green:#7dbd3c;
  --brand-green:#add136;
  --yellow:#f9b418;
  --orange:#ef5322;
  --blue:#3a9ad9;
  --ink:#222;
  --muted:#555;
  --dark:#1c1c1c;
  --field:#333;
  --white:#fff;
}
*{box-sizing:border-box;margin:0;padding:0}
html,body{width:1200px;height:2611px;overflow:hidden;background:var(--white);font-family:"Roboto",Arial,sans-serif;color:var(--ink)}
.page{position:relative;width:1200px;height:2611px}
.abs{position:absolute}

/* header */
.site-header{left:0;top:0;width:1200px;height:95px;background:var(--white);border-bottom:4px solid var(--brand-green)}
.brand{left:100px;top:20px;height:60px;display:flex;align-items:center;gap:10px}
.brand-mark{width:22px;height:22px;border-radius:50%;background:var(--green)}
.brand-name{font-size:24px;font-weight:700;color:var(--green);line-height:1}
.brand-sub{font-size:10px;letter-spacing:3px;color:var(--muted);font-weight:400;display:block;margin-top:4px}
.phone{right:100px;top:14px;font-size:25px;font-weight:500;color:#111}
.main-nav{right:100px;top:62px;display:flex;gap:34px;font-size:12px;color:var(--green)}
.main-nav a{color:inherit;text-decoration:none;padding-bottom:8px}
.main-nav a.active{border-bottom:3px solid var(--green)}

/* hero */
.hero{left:0;top:99px;width:1200px;height:371px;background:linear-gradient(100deg,#6f7f8a 0%,#a9b6be 45%,#d8dde0 70%,#8c949a 100%)}
.hero-panel{left:98px;top:49px;width:538px;height:258px;background:rgba(86,150,210,.78);padding:24px 24px;color:var(--white)}
.hero-panel h1{font-size:33px;font-weight:300;line-height:1.15}
.hero-panel p{font-size:16px;font-weight:300;line-height:1.55;margin-top:22px}
.btn-outline{display:inline-block;margin-top:22px;border:2px solid var(--white);color:var(--white);font-size:14px;font-weight:500;padding:9px 22px}

/* headings */
.section-title{font-size:33px;font-weight:300;color:#222}
.center{left:0;width:1200px;text-align:center}

/* services */
.service{color:var(--white);padding:14px 22px}
.service h3{font-size:23px;font-weight:400;line-height:1.15}
.service p{font-size:11px;line-height:1.45;margin-top:8px;max-width:300px}
.service svg{position:absolute}
.hitech{left:98px;top:568px;width:322px;height:187px;background:var(--yellow)}
.industrial{left:432px;top:568px;width:334px;height:344px;background:var(--green)}
.banking{left:778px;top:568px;width:322px;height:204px;background:var(--orange)}
.healthcare{left:98px;top:768px;width:322px;height:210px;background:var(--blue)}

/* clients */
.clients{left:0;top:1135px;width:1200px;height:70px;display:flex;justify-content:space-between;align-items:center;padding:0 0 0 0}
.client{font-size:34px;font-weight:500;color:#666;letter-spacing:1px}

/* testimonials */
.testimonials{left:0;top:1243px;width:1200px;height:367px;background:linear-gradient(135deg,#2c2c2c,#4a4642 50%,#2a2a2a)}
.testimonials .section-title{color:rgba(255,255,255,.75)}
.quote-panel{left:98px;top:95px;width:1000px;height:209px;background:rgba(125,189,60,.88)}
.portrait{left:0;top:0;width:167px;height:147px;background:linear-gradient(180deg,#c9ccd0,#6b7078)}
.caption{left:0;top:147px;width:167px;height:62px;background:var(--white);text-align:center;padding-top:12px}
.caption strong{display:block;font-size:15px;font-weight:500;color:#111}
.caption span{font-size:11px;color:#444}
.quote{font-size:18px;color:var(--white);line-height:1.45}

/* contact */
.contact-col{width:300px;text-align:center;font-size:15px;font-weight:500;line-height:1.4;color:#111}
.contact-col svg{display:block;margin:0 auto 22px}
.map{left:0;top:2075px;width:1200px;height:400px;background:linear-gradient(120deg,#c9cdc4,#b4b8ae 50%,#c4c8be);opacity:.95}
.contact-form{left:98px;top:1915px;width:1002px;height:257px;background:var(--dark)}
.field{background:var(--field);color:var(--white);font-size:11px;padding:12px 14px;font-weight:500}
.submit{left:450px;top:180px;width:104px;height:35px;border:2px solid var(--white);color:var(--white);font-size:11px;display:flex;align-items:center;justify-content:center}

/* footer */
.site-footer{left:0;top:2475px;width:1200px;height:136px;background:#222;color:var(--white)}
.social{left:0;top:44px;width:1200px;display:flex;justify-content:center;gap:30px}
.social span{width:12px;height:12px;border-radius:50%;background:var(--white)}
.copyright{top:88px;font-size:13px}
</style>
</head>
<body>
<div class="page">

  <header class="site-header abs">
    <div class="brand abs">
      <span class="brand-mark"></span>
      <span class="brand-name">BrightLane<span class="brand-sub">CONSULTANTS</span></span>
    </div>
    <div class="phone abs">(123) 555 0142</div>
    <nav class="main-nav abs">
      <a class="active">HOME</a><a>PRODUCTS</a><a>ABOUT US</a><a>OUTSOURCING</a><a>CONTACT US</a>
    </nav>
  </header>

  <section class="hero abs" role="img" aria-label="Businesswoman on a bench checking her phone and holding a coffee cup">
    <div class="hero-panel abs">
      <h1>Outsourcing Individual talent<br>for all kinds of Business</h1>
      <p>Our services are fully managed and we<br>view ourselves as IT department of our company</p>
      <span class="btn-outline">REQUEST A QUOTE</span>
    </div>
  </section>

  <h2 class="section-title abs" style="left:100px;top:500px">Our Services</h2>

  <article class="service hitech abs">
    <h3>Hi-Tech</h3>
    <p>Efficient people suitable for challenging positions in the hi-tech industry</p>
    <svg style="left:22px;top:110px" width="46" height="50" viewBox="0 0 46 50" fill="none" stroke="#fff" stroke-width="2.4"><path d="M8 4 L16 4 L19 14 L13 18 Q17 30 28 36 L32 30 L42 33 L42 42 Q36 48 28 46 Q8 38 3 14 Q3 6 8 4Z"/></svg>
    <svg style="left:272px;top:124px" width="28" height="28" viewBox="0 0 28 28" fill="none" stroke="#fff" stroke-width="2.2"><circle cx="14" cy="14" r="12"/><path d="M9 14h10M15 9l5 5-5 5"/></svg>
  </article>

  <article class="service industrial abs">
    <h3>Industrial and<br>Engineering</h3>
    <p>Specialist in knowledge and vastly experienced for the precise expertise in producing cutting edge solutions</p>
    <svg style="left:22px;top:200px" width="120" height="110" viewBox="0 0 120 110" fill="none" stroke="#fff" stroke-width="2.4"><rect x="4" y="6" width="46" height="32" rx="3"/><path d="M20 38v8M14 46h20"/><circle cx="80" cy="76" r="22"/><path d="M58 76h44M80 54v44M66 62q14 8 28 0M66 90q14-8 28 0M80 54q-12 22 0 44M80 54q12 22 0 44"/><path d="M60 12q28 0 36 30M92 36l4 7 6-6"/><path d="M50 100q-30 0-38-34M16 72l-4-7-6 6"/></svg>
    <svg style="left:284px;top:290px" width="28" height="28" viewBox="0 0 28 28" fill="none" stroke="#fff" stroke-width="2.2"><circle cx="14" cy="14" r="12"/><path d="M9 14h10M15 9l5 5-5 5"/></svg>
  </article>

  <article class="service banking abs">
    <h3>Banking and Financial</h3>
    <p>Security and flexibility is important aspect and we are bound to that by outsourching extremely qualified individuals</p>
    <svg style="left:22px;top:128px" width="60" height="50" viewBox="0 0 60 50" fill="none" stroke="#fff" stroke-width="2.4"><rect x="4" y="4" width="50" height="36" rx="4"/><rect x="22" y="10" width="16" height="22" rx="2"/><path d="M4 30h50"/></svg>
    <svg style="left:272px;top:142px" width="28" height="28" viewBox="0 0 28 28" fill="none" stroke="#fff" stroke-width="2.2"><circle cx="14" cy="14" r="12"/><path d="M9 14h10M15 9l5 5-5 5"/></svg>
  </article>

  <article class="service healthcare abs">
    <h3>Healthcare and<br>Consumer/FMCG</h3>
    <p>Offering both talented and experienced, we know we have the perfect fit for your business</p>
    <svg style="left:22px;top:130px" width="60" height="56" viewBox="0 0 60 56" fill="none" stroke="#fff" stroke-width="2.4"><path d="M8 12 L15 12 L18 21 L13 25 Q16 35 26 40 L30 35 L38 38 L38 46 Q33 51 26 49 Q8 42 4 22 Q4 14 8 12Z"/><rect x="28" y="4" width="28" height="18" rx="4"/><circle cx="35" cy="13" r="1.4" fill="#fff"/><circle cx="42" cy="13" r="1.4" fill="#fff"/><circle cx="49" cy="13" r="1.4" fill="#fff"/></svg>
    <svg style="left:272px;top:148px" width="28" height="28" viewBox="0 0 28 28" fill="none" stroke="#fff" stroke-width="2.2"><circle cx="14" cy="14" r="12"/><path d="M9 14h10M15 9l5 5-5 5"/></svg>
  </article>

  <h2 class="section-title abs center" style="top:1055px">Our Clients</h2>
  <div class="clients abs">
    <span class="client" style="margin-left:-40px">Tessvar</span>
    <span class="client">Oriel</span>
    <span class="client">Halden</span>
    <span class="client">Quillet</span>
    <span class="client" style="margin-right:-40px">Kivomark</span>
  </div>

  <section class="testimonials abs" role="img" aria-label="Desk scene with laptop, keyboard, sunglasses and coffee, darkened">
    <h2 class="section-title abs center" style="top:22px">Testimonials</h2>
    <div class="quote-panel abs">
      <div class="portrait abs" role="img" aria-label="Portrait of a man in a suit"></div>
      <div class="caption abs"><strong>SOME PERSON</strong><span>CEO OF SOME COMPANY</span></div>
      <p class="quote abs" style="left:180px;top:36px">mple Text Sample Text Sample Text<br>ext Sample Text</p>
      <p class="quote abs" style="left:655px;top:36px;text-align:right;width:345px;white-space:nowrap;overflow:hidden">Sample Text Sample Text Sample Text Sam<br>Sample Text Sample Text</p>
      <svg class="abs" style="left:548px;top:138px" width="64" height="26" viewBox="0 0 64 26" fill="none" stroke="#fff" stroke-width="2"><path d="M20 3 L6 13 L20 23Z"/><path d="M42 3 L56 13 L42 23Z"/></svg>
    </div>
  </section>

  <h2 class="section-title abs center" style="top:1643px">Contact Us</h2>

  <div class="contact-col abs" style="left:115px;top:1718px">
    <svg width="52" height="60" viewBox="0 0 52 60" fill="none" stroke="#f9a825" stroke-width="2.2"><rect x="6" y="6" width="28" height="48" rx="4"/><path d="M16 48h8"/><rect x="24" y="16" width="24" height="16" rx="3"/><circle cx="30" cy="24" r="1.2" fill="#f9a825"/><circle cx="36" cy="24" r="1.2" fill="#f9a825"/><circle cx="42" cy="24" r="1.2" fill="#f9a825"/></svg>
    Phone No<br>Phone No
  </div>
  <div class="contact-col abs" style="left:448px;top:1718px">
    <svg width="56" height="60" viewBox="0 0 56 60" fill="none" stroke="#e8452a" stroke-width="2.2"><circle cx="28" cy="36" r="8"/><path d="M12 58q0-14 16-14t16 14"/><path d="M34 4h18v14H42l-4 5v-5h-4Z"/><path d="M4 24q0-10 10-10t10 10q0 8-10 18Q4 32 4 24Z"/></svg>
    Address line 1<br>Address line 2<br>Address line 3
  </div>
  <div class="contact-col abs" style="left:780px;top:1718px">
    <svg width="60" height="60" viewBox="0 0 60 60" fill="none" stroke="#7e57c2" stroke-width="2.2"><circle cx="30" cy="30" r="24"/><path d="M6 30h48M30 6v48M30 6q-14 24 0 48M30 6q14 24 0 48"/><path d="M40 22q0-8 8-8t8 8q0 6-8 14q-8-8-8-14Z" fill="#fff"/></svg>
    support@brightlane.example<br><span style="color:#1e4fa0">hello@brightlane.example</span>
  </div>

  <div class="map abs" role="img" aria-label="Street map showing the office location"></div>

  <form class="contact-form abs">
    <div class="field abs" style="left:50px;top:43px;width:438px;height:45px">Name*</div>
    <div class="field abs" style="left:50px;top:103px;width:438px;height:45px">E-mail*</div>
    <div class="field abs" style="left:518px;top:43px;width:430px;height:105px">Message</div>
    <div class="submit abs">SUBMIT</div>
  </form>

  <footer class="site-footer abs">
    <div class="social abs"><span></span><span></span><span></span><span></span><span></span></div>
    <p class="copyright abs center">Copyright goes here</p>
  </footer>

</div>
</body>
</html>
```